lumbrett-scope virtual tours is looking for a website redisgn that uses our new logo

Using LBS's logo as a basis, please redesign our website. Our web application developer has a stand-in site up at www.lb-scope.net. LBS is a virtual tour company whose main clients are the owners of real estate and rental properties; however, LBS will produce virtual tours for any person, company, or organization for whatever purpose they see fit to use the tour for. This is a dynamic website consisting of three pages. An index/info page, a contact/web form page, a price listing page, a template for a tour page which will have a height/width 75% iframe that showcases one of our tours (www.lb-scope.net) for an example. What is needed: HTML template design for pages that incorporates logo, custom graphic for mail link, FB link, Twitter link, and Virtual Tour link. We would also like a watermarked developed out of our logo pin (.ai of logo pin included). The watermark should also include the capital letters LBS, be in grayscale, translucent and the masked.
Target Market(s)
Home Owners, Real Estate Agents, Property Managers, Event Managers, Business Owners, Park Owners,
Industry/Entity Type
Real Estate
Number of Pages Required
3 page
Requirements
Must have
- New web design that uses our logo (file included). Must have a custom watermark that uses our custom logo pin (file included). Watermark should be gray scale, translucent, and masked. Custom graphics for homepage link (would like something that uses our logo pin), mail link, facebook link, and twitter link.
Nice to have
- I've uploaded a pdf called pano_vs_spherical.pdf which is a scan of a crude drawing I did that illustrates what we'd like for our info page. Basically we'd like to describe the difference between a panoramic image and a spherical image and to do so we'd like to have some graphical drawings that illustrate which each is. We'd like two separate image files that we can include on our info page. Use the uploaded .pdf as a guide. Would also like images 0-9 of custom numerals that match the theme of the page to be used as part of a visitor counter script.
Should not have
- Do not need html code or stylesheets (css). Would rather you concentrate on graphic design of custom graphics, layout, and color scheme. We have competent web applications developers in our small company who can code, we just need you, the graphic artist to work your magic.

```html
<!DOCTYPE html>
<html lang="en">
<head>
<meta charset="utf-8">
<title>lumbrett-scope virtual tours</title>
<link rel="stylesheet" href="https://fonts.googleapis.com/css2?family=Source+Sans+3:wght@400;600;700&display=swap">
<style>
  :root {
    --orange: #e36a3c;
    --orange-dark: #c9552a;
    --ink: #1f1f1f;
    --text: #2b2b2b;
    --nav-top: #3a3a3a;
    --nav-bottom: #111111;
    --tab-bg: #5f6166;
    --footer: #2a2a2a;
    --page: #ffffff;
    --plan-light: #f4f4f4;
    --plan-mid: #e6e6e6;
    --white: #ffffff;
  }
  * { box-sizing: border-box; margin: 0; padding: 0; }
  html, body { width: 1200px; height: 896px; overflow: hidden; background: var(--page); }
  body { position: relative; font-family: "Source Sans 3", Arial, sans-serif; color: var(--text); }

  .top-rule { position: absolute; left: 0; top: 0; width: 1200px; height: 4px; background: var(--orange); }

  .masthead {
    position: absolute; left: 0; top: 4px; width: 1200px; height: 146px;
    background: radial-gradient(ellipse at center, var(--plan-light) 0%, var(--plan-mid) 100%);
  }
  .brand {
    position: absolute; left: 440px; top: 30px; display: flex; align-items: center; gap: 14px;
  }
  .brand-dot { width: 44px; height: 44px; border-radius: 50%; background: var(--orange); }
  .brand-name {
    font-weight: 700; color: var(--ink); font-size: 40px; line-height: 38px; letter-spacing: -0.5px;
  }
  .brand-name small { display: block; font-size: 15px; line-height: 18px; letter-spacing: 2px; text-align: right; }

  .main-nav {
    position: absolute; left: 0; top: 150px; width: 1200px; height: 44px;
    background: linear-gradient(var(--nav-top), var(--nav-bottom));
  }
  .main-nav ul { list-style: none; position: absolute; left: 152px; top: 0; display: flex; height: 44px; }
  .main-nav li {
    height: 44px; display: flex; align-items: center; justify-content: center;
    color: var(--white); font-size: 17px; font-weight: 600; border-right: 1px solid #4a4a4a;
  }
  .main-nav li.is-active { background: var(--orange); color: var(--ink); }
  .nav-home { width: 102px; }
  .nav-contact { width: 143px; }
  .nav-pricing { width: 117px; }

  .social { position: absolute; left: 930px; top: 6px; display: flex; gap: 4px; }
  .social span {
    width: 32px; height: 32px; border-radius: 50%; border: 2px solid var(--white);
    display: flex; align-items: center; justify-content: center;
  }
  .social .social-b { background: var(--orange); }

  .welcome {
    position: absolute; left: 0; top: 236px; width: 1200px; text-align: center;
    font-size: 32px; font-weight: 400; color: var(--ink);
  }
  .welcome strong { font-weight: 700; }

  .tour { position: absolute; left: 152px; top: 284px; width: 896px; height: 425px; }
  .tour-tabs { display: flex; height: 36px; background: var(--tab-bg); list-style: none; }
  .tour-tabs li {
    display: flex; align-items: center; justify-content: center;
    color: var(--white); font-size: 14px; text-transform: uppercase;
  }
  .tour-tabs li.is-active { background: var(--orange); color: var(--ink); }
  .tour-view {
    position: relative; height: 389px;
    background: linear-gradient(180deg, #5a4a3c 0%, #b8ab98 38%, #e8e2d8 62%, #6d6258 100%);
  }
  .tour-view::after {
    content: ""; position: absolute; right: 0; top: 0; width: 190px; height: 335px;
    background: linear-gradient(90deg, #c9d3d8, #eef2f3);
  }
  .view-icon { position: absolute; z-index: 2; }
  .controls {
    position: absolute; z-index: 2; left: 0; bottom: 0; width: 896px; height: 54px;
    background: rgba(20, 20, 20, 0.55);
  }
  .player-badge {
    position: absolute; left: 12px; top: 10px; width: 102px; height: 36px; background: var(--white);
    display: flex; align-items: center; justify-content: center; gap: 5px;
    font-size: 12px; font-weight: 700; color: var(--ink);
  }
  .player-badge i { width: 10px; height: 10px; border-radius: 50%; background: var(--orange); }
  .control-icons { position: absolute; left: 466px; top: 14px; }

  .intro {
    position: absolute; left: 168px; top: 734px; width: 864px; text-align: center;
    font-size: 14.5px; line-height: 22px; color: var(--text);
  }
  .intro a { color: var(--orange); text-decoration: none; }

  .site-footer {
    position: absolute; left: 0; top: 848px; width: 1200px; height: 48px; background: var(--footer);
    color: var(--white); font-size: 13.5px; display: flex; align-items: center; justify-content: center;
  }
  .site-footer strong { font-weight: 700; margin-right: 5px; }
  .site-footer .sep { margin: 0 7px; }
</style>
</head>
<body>
  <div class="top-rule"></div>

  <header class="masthead" role="img" aria-label="Faint architectural floor plan background in light grey">
    <div class="brand">
      <span class="brand-dot"></span>
      <div class="brand-name">lumbrett-scope<small>virtual tours</small></div>
    </div>
  </header>

  <nav class="main-nav">
    <ul>
      <li class="nav-home is-active">HOME</li>
      <li class="nav-contact">CONTACT US</li>
      <li class="nav-pricing">PRICING</li>
    </ul>
    <div class="social">
      <span class="social-a" aria-label="Social link"></span>
      <span class="social-b" aria-label="Social link"></span>
      <span class="social-mail" aria-label="Mail">
        <svg width="18" height="13" viewBox="0 0 18 13"><rect x="1" y="1" width="16" height="11" fill="none" stroke="#fff" stroke-width="1.6"/><path d="M1 1 L9 7.5 L17 1" fill="none" stroke="#fff" stroke-width="1.6"/></svg>
      </span>
    </div>
  </nav>

  <h1 class="welcome">Welcome to <strong>lumbrett</strong>-scope Virtual Tours</h1>

  <section class="tour">
    <ul class="tour-tabs">
      <li style="width:129px">Fornt Entry</li>
      <li class="is-active" style="width:119px">Living Room</li>
      <li style="width:87px">Kitchen</li>
      <li style="width:104px">Back Patio</li>
      <li style="width:110px">Bedroom 1</li>
      <li style="width:112px">Bathroom</li>
      <li style="width:90px">Bedroom 2</li>
      <li style="width:145px">Top of Stairs</li>
    </ul>
    <div class="tour-view" role="img" aria-label="Panoramic photo of a modern living room with TV wall, glass table and balcony doors">
      <svg class="view-icon" style="left:186px;top:70px" width="36" height="30" viewBox="0 0 36 30">
        <rect x="0" y="6" width="36" height="24" rx="3" fill="#e36a3c"/><rect x="11" y="1" width="14" height="7" rx="2" fill="#e36a3c"/>
        <circle cx="18" cy="18" r="7" fill="none" stroke="#fff" stroke-width="2.5"/>
      </svg>
      <svg class="view-icon" style="left:772px;top:82px" width="34" height="34" viewBox="0 0 34 34" fill="none" stroke="#e36a3c" stroke-width="3">
        <path d="M2 11V2h9M23 2h9v9M32 23v9h-9M11 32H2v-9"/><rect x="10" y="10" width="14" height="14"/>
      </svg>
      <div class="controls">
        <div class="player-badge"><i></i>lumbrett-scope</div>
        <svg class="control-icons" width="418" height="26" viewBox="0 0 418 26" fill="#fff" stroke="#fff">
          <path d="M11 2v22M0 13h22" stroke-width="4"/>
          <path d="M32 13h22" stroke-width="4"/>
          <path d="M71 2v12" stroke-width="5"/><path d="M63 12h16l-8 11z" stroke="none"/>
          <path d="M103 24V12" stroke-width="5"/><path d="M95 14h16l-8-11z" stroke="none"/>
          <path d="M147 13h-12" stroke-width="5"/><path d="M137 5v16l-11-8z" stroke="none"/>
          <path d="M159 13h12" stroke-width="5"/><path d="M169 5v16l11-8z" stroke="none"/>
          <path d="M200 24c-4-3-8-8-8-12M200 24h8c3-3 4-7 4-14M196 12V4M201 11V2M206 11V4M211 12V7" fill="none" stroke-width="2"/>
          <path d="M245 6a9 9 0 1 0 3 10" fill="none" stroke-width="3.5"/><path d="M241 1l9 4-5 7z" stroke="none"/>
          <text x="262" y="23" font-family="Source Sans 3, Arial, sans-serif" font-size="27" font-weight="700" stroke="none">?</text>
          <path d="M286 13c5-7 15-7 20 0-5 7-15 7-20 0z" fill="none" stroke-width="2.5"/><path d="M288 23L305 3" stroke-width="2.5"/>
          <path d="M320 9h5l7-6v20l-7-6h-5z" stroke="none"/><path d="M336 8c3 3 3 7 0 10M340 5c5 5 5 11 0 16" fill="none" stroke-width="2"/>
          <path d="M356 3h7M356 3v7M374 3h-7M374 3v7M356 23h7M356 23v-7M374 23h-7M374 23v-7M358 5l5 5M372 5l-5 5M358 21l5-5M372 21l-5-5" fill="none" stroke-width="2.5"/>
        </svg>
      </div>
    </div>
  </section>

  <p class="intro">Sed ut perspiciatis unde omnis iste natus error sit voluptatem accusantium doloremque laudantium, totam rem aperiam, eaque ipsa quae ab illo inventore veritatis et quasi <a href="#">architecto</a> beatae vitae dicta sunt explicabo. Nemo enim <a href="#">ipsam voluptatem quia voluptas</a> sit aspernatur aut odit aut fugit, sed quia consequuntur magni dolores eos qui ratione voluptatem sequi nesciunt. Neque porro quisquam est, qui dolorem ipsum quia dolor sit amet, consectetur, adipisci velit, sed quia non numquam eius modi tempora incidunt ut labore et dolore magnam.</p>

  <footer class="site-footer">© 2015. <strong>&nbsp;lumbrett-scope Virtual Tours.</strong> Terms &amp; Conditions<span class="sep">|</span>Privacy Policy.</footer>
</body>
</html>
```